Business card design needed

We do excavation, cartage and contracting
I would quote like to have a picture of my digger as the whole back ground and the words on top. If that looks any good
Otherwise please feel free to come up with any other cool options

Cheers Marc

KLR Contracting
Excavation, Cartage, Contracting
Marcus Prewitt
www.klr-example.co.nz
021 584 067
marc@klr-example.co.nz

```html
<!DOCTYPE html>
<html lang="en">
<head>
<meta charset="utf-8">
<title>KLR Contracting – Business Card</title>
<link rel="stylesheet" href="https://fonts.googleapis.com/css2?family=Bebas+Neue&family=Roboto:wght@300;400&display=swap">
<style>
  :root {
    --backdrop: #8e8e8c;
    --card-dark: #1e1f1f;
    --card-mid: #3a3b3b;
    --brand-green: #1fa31f;
    --bar-green: #1c7d1c;
    --hazard-yellow: #c9a21a;
    --hazard-dark: #7a6212;
    --text-light: #f2f2f2;
  }
  * { margin: 0; padding: 0; box-sizing: border-box; }
  html, body {
    width: 1200px; height: 900px; overflow: hidden;
    background: var(--backdrop);
  }
  .stage { position: relative; width: 1200px; height: 900px; }
  .card {
    position: absolute; width: 572px; height: 353px; overflow: hidden;
    background: radial-gradient(ellipse at 40% 35%, var(--card-mid), var(--card-dark) 75%);
    box-shadow: 0 6px 16px rgba(0,0,0,.45);
  }
  .card--front { left: 51px; top: 125px; z-index: 2; }
  .card--back { left: 567px; top: 446px; z-index: 1; }

  .hazard-band { position: absolute; inset: 0; width: 100%; height: 100%; }

  .holder-name {
    position: absolute; left: 57px; top: 42px;
    font-family: "Bebas Neue", sans-serif; font-size: 44px; letter-spacing: 1px;
    color: var(--text-light); line-height: 1;
  }
  .holder-name .surname { color: var(--brand-green); }
  .services-bar {
    position: absolute; left: 0; top: 87px; width: 359px; height: 25px;
    background: linear-gradient(90deg, var(--bar-green) 85%, rgba(28,125,28,.4));
    font-family: "Bebas Neue", sans-serif; font-size: 16px; letter-spacing: .4px;
    color: var(--text-light); line-height: 25px; padding-left: 57px;
  }
  .contact-list { position: absolute; left: 60px; top: 160px; list-style: none; }
  .contact-list li {
    display: flex; align-items: center; gap: 12px; height: 31px;
    font-family: "Roboto", sans-serif; font-weight: 300; font-size: 19px;
    color: var(--text-light);
  }
  .contact-icon { width: 20px; height: 20px; flex: none; }

  .brand-name {
    position: absolute;
    font-family: "Bebas Neue", sans-serif; color: var(--brand-green);
    line-height: 1; letter-spacing: 2px;
  }
  .card--front .brand-name { left: 378px; top: 100px; font-size: 92px; }
  .card--back .brand-name { left: 92px; top: 232px; font-size: 74px; }

  .digger-photo {
    position: absolute; inset: 0;
    background:
      radial-gradient(ellipse at 70% 40%, rgba(200,200,200,.35), transparent 55%),
      linear-gradient(180deg, #2b2c2c 0%, #3c3d3d 45%, #1b1b1b 100%);
  }
  .web-address {
    position: absolute; left: 0; width: 280px; top: 322px; text-align: center;
    font-family: "Roboto", sans-serif; font-size: 15px; color: var(--text-light);
  }
</style>
</head>
<body>
<div class="stage">

  <section class="card card--front">
    <svg class="hazard-band" viewBox="0 0 572 353" role="img" aria-label="Diagonal yellow and black hazard stripe band">
      <defs>
        <linearGradient id="hazardFront" x1="0" y1="0" x2="1" y2="0">
          <stop offset="0" stop-color="var(--hazard-dark)"/>
          <stop offset=".5" stop-color="var(--hazard-yellow)"/>
          <stop offset="1" stop-color="var(--hazard-dark)"/>
        </linearGradient>
      </defs>
      <polygon points="0,267 572,227 572,285 0,322" fill="url(#hazardFront)" opacity=".85"/>
    </svg>

    <h1 class="holder-name">Marcus <span class="surname">Prewitt</span></h1>
    <div class="services-bar">KLR Contracting Excavation, Cartage, Contracting</div>

    <ul class="contact-list">
      <li>
        <svg class="contact-icon" viewBox="0 0 20 20"><rect width="20" height="20" rx="3" fill="var(--brand-green)"/><path d="M6 4.5l2 .3 1 2.7-1.4 1a7 7 0 0 0 3.9 3.9l1-1.4 2.7 1 .3 2c-.3.9-1.2 1.5-2.2 1.5A9.5 9.5 0 0 1 4.5 6.7C4.5 5.7 5.1 4.8 6 4.5z" fill="#1e1f1f"/></svg>
        021 584 067
      </li>
      <li>
        <svg class="contact-icon" viewBox="0 0 20 20"><rect x="1" y="4" width="18" height="12" rx="1.5" fill="var(--brand-green)"/><path d="M1.5 5l8.5 6 8.5-6" fill="none" stroke="#1e1f1f" stroke-width="1.5"/></svg>
        marc@klr-example.co.nz
      </li>
      <li>
        <svg class="contact-icon" viewBox="0 0 20 20"><circle cx="10" cy="10" r="9" fill="var(--brand-green)"/><path d="M1 10h18M10 1c3 3 3 15 0 18M10 1c-3 3-3 15 0 18" fill="none" stroke="#1e1f1f" stroke-width="1.2"/></svg>
        www.klr-example.co.nz
      </li>
    </ul>

    <div class="brand-name">KLR</div>
  </section>

  <section class="card card--back">
    <div class="digger-photo" role="img" aria-label="Black and white photo of an excavator digging on a work site"></div>
    <svg class="hazard-band" viewBox="0 0 572 353" role="img" aria-label="Diagonal yellow and black hazard stripe band">
      <defs>
        <linearGradient id="hazardBack" x1="0" y1="0" x2="1" y2="0">
          <stop offset="0" stop-color="var(--hazard-dark)"/>
          <stop offset=".6" stop-color="var(--hazard-yellow)"/>
          <stop offset="1" stop-color="var(--hazard-dark)"/>
        </linearGradient>
      </defs>
      <polygon points="0,174 572,119 572,164 0,224" fill="url(#hazardBack)" opacity=".85"/>
    </svg>
    <div class="brand-name">KLR</div>
    <p class="web-address">www.klr-example.co.nz</p>
  </section>

</div>
</body>
</html>
```